Business Card for my New Brokerage

Looking to get a business card design for my new Real Estate Brokerage.
I want it with Picture, Phone Number, Email, Website, Office Address
Name and Designation. Please add logo too.

Target Market(s)

Real Estate Investors or Home Buyers

Industry/Entity Type

Real Estate

Contact Information for Business Card

Name, Email, Phone Number, website, email, office address

Colors
EB3D1F
EC4F4E
F09395
F8D3D4
FCEDEE

Requirements
Must have
• Minimalistic, Clean, Modern, Photo
Nice to have
• White and Red Colors

```html
<!DOCTYPE html>
<html lang="en">
<head>
<meta charset="utf-8">
<title>Ember Realty Inc — Business Card</title>
<link href="https://fonts.googleapis.com/css2?family=Jost:wght@400;500&family=Montserrat:wght@700&display=swap" rel="stylesheet">
<style>
  :root {
    --backdrop: #d9d9d9;
    --card: #2a2a2b;
    --edge: #e00c0c;
    --gold: #d4ad55;
    --gold-light: #f3df96;
    --gold-dark: #a9802f;
    --ink-light: #f1f1f1;
  }
  * { margin: 0; padding: 0; box-sizing: border-box; }
  html, body {
    width: 1200px; height: 800px; overflow: hidden;
    background: var(--backdrop);
  }
  .canvas {
    width: 1200px; height: 800px;
    display: flex; align-items: center; justify-content: center; gap: 50px;
  }
  .card {
    position: relative;
    width: 540px; height: 309px;
    background: var(--card);
    border-bottom: 3px solid var(--edge);
    border-right: 2px solid var(--edge);
    box-shadow: 0 14px 30px rgba(0,0,0,0.28);
    overflow: hidden;
  }

  /* Contact side */
  .feature-area {
    position: absolute; left: 0; top: 0; bottom: 0; width: 170px;
    background: linear-gradient(180deg, var(--gold-dark) 0%, var(--gold-light) 50%, var(--gold) 100%);
  }
  .identity {
    position: absolute; right: 36px; top: 40px; text-align: right;
  }
  .identity .person-name {
    font-family: "Montserrat", sans-serif; font-weight: 700;
    font-size: 22px; letter-spacing: 0.5px; color: var(--gold);
    text-transform: uppercase;
  }
  .identity .person-role {
    font-family: "Jost", sans-serif; font-size: 15px; color: var(--ink-light);
    margin-top: 2px;
  }
  .address {
    position: absolute; right: 36px; top: 132px; text-align: right;
    font-family: "Jost", sans-serif; font-size: 14px; line-height: 1.35;
    color: var(--ink-light);
  }
  .contact-list {
    position: absolute; right: 36px; top: 186px; list-style: none;
    font-family: "Jost", sans-serif; font-size: 14px; line-height: 1.45;
    color: var(--ink-light);
  }
  .contact-list li {
    display: flex; align-items: center; justify-content: flex-end; gap: 10px;
  }
  .contact-list svg { width: 13px; height: 13px; flex: none; }

  /* Brand side */
  .brand {
    position: absolute; inset: 0;
    display: flex; align-items: center; justify-content: center; gap: 14px;
  }
  .brand .brand-dot {
    width: 14px; height: 14px; border-radius: 50%; background: var(--edge);
  }
  .brand .brand-name {
    font-family: "Jost", sans-serif; font-weight: 400;
    font-size: 36px; color: var(--ink-light);
  }
</style>
</head>
<body>
<main class="canvas">

  <section class="card card-contact">
    <div class="feature-area" role="img" aria-label="Large gold brand emblem decoration"></div>

    <div class="identity">
      <p class="person-name">Daniel Brooks</p>
      <p class="person-role">Founder &amp; CEO</p>
    </div>

    <p class="address">2816 Willow Crest Road<br>Anchorage, Alaska 99508</p>

    <ul class="contact-list">
      <li>555-201-4478
        <svg viewBox="0 0 16 16" aria-hidden="true"><path fill="var(--gold)" d="M3 1.5l2.5-.5 1.5 3.5-1.8 1.2a9 9 0 0 0 5 5l1.2-1.8 3.5 1.5-.5 2.5c-.3 1-1.3 1.5-2.4 1.3C6.8 13.4 2.6 9.2 1.7 3.9 1.5 2.8 2 1.8 3 1.5z"/></svg>
      </li>
      <li>555-318-2290
        <svg viewBox="0 0 16 16" aria-hidden="true"><rect x="4" y="1" width="8" height="14" rx="1.5" fill="none" stroke="var(--gold)" stroke-width="1.6"/><circle cx="8" cy="12.5" r="0.9" fill="var(--gold)"/></svg>
      </li>
      <li>info@emberrealty.com
        <svg viewBox="0 0 16 16" aria-hidden="true"><rect x="1" y="3" width="14" height="10" rx="1" fill="var(--gold)"/><path d="M1.5 3.8L8 9l6.5-5.2" fill="none" stroke="var(--card)" stroke-width="1.3"/></svg>
      </li>
      <li>www.emberrealty.com
        <svg viewBox="0 0 16 16" aria-hidden="true"><circle cx="8" cy="8" r="6.5" fill="none" stroke="var(--gold)" stroke-width="1.5"/><ellipse cx="8" cy="8" rx="2.6" ry="6.5" fill="none" stroke="var(--gold)" stroke-width="1.2"/><path d="M1.5 8h13" stroke="var(--gold)" stroke-width="1.2"/></svg>
      </li>
    </ul>
  </section>

  <section class="card card-brand">
    <div class="brand">
      <span class="brand-dot" aria-hidden="true"></span>
      <p class="brand-name">Ember Realty Inc</p>
    </div>
  </section>

</main>
</body>
</html>
```